Fernmoor PTA Website Design

We are working with Fernmoor Elementary School PTA. They are a Parent Teacher Association that needs a new website design.

A Parent Teacher Association (PTA) is a volunteer organization that brings parents, teachers, and school staff together to support students and enhance their educational experience. PTAs organize fundraisers, sponsor school events, advocate for education policies, and foster stronger connections between families and schools.

Some sites to use for inspiration:

https://clubvane.com/demo/
https://nonprofits.fundrova.com/blogs/more-great-pta-websites-you-should-copy
https://www.qerbrix.com

Thank you for taking the time to consider designing a website for us. We are web developers based in Stockton and Los Angeles, CA, USA. Most of our projects go through the same process. Understanding this process may help you win a project with us. We custom-code all of our websites in-house. We don’t have any requirements as to what tools you use for your design, but we prefer Figma files. For any design that we label as four-stars, we send it to the client for review. The client picks the final design they want us to use. Once we complete this process, we will continue to show additional clients all the four-star sites and purchase them later. Your designs will have multiple chances to sell. For better chances of success, we ask that you follow these guidelines.

IMAGES:
If you use any images or icons in the design, we ask that you have a link to the asset so we can purchase the image/icon. Most of the designs we submit do not have the customer’s images on them unless they have some great images. Be creative; show us the feeling you are trying to portray with your image choices. Use any royalty-free site you choose. We subscribe to Vexiq and mainly use their images, but we can purchase images outside of Vexiq.

PLEASE NOTE: we will not submit designs to clients with watermarks on the images.

FONTS:
We ask that you identify the fonts used in the design. This can be done in a message if you want. We typically use Tarnel Fonts and Vexiq Fonts.

CONTENT:
We're always open to different content and ideas. We often submit designs with stock images so the client can see our vision. We typically take pictures after the website launch to use their images with our vision. Lorem Ipsum is fine for paragraphs, but we ask that you write the headers in correct English. We want to be able to show the vision and identify the sections of the website.

INSPIRATION:
We typically add a couple of links in the brief of websites we like to help you get started in your design.

REVISIONS:
We do not often ask for revisions of the designs unless we see something in the design that may not appeal to the client. If there are slight changes that we want to make, we do that in the development process.

FEEDBACK:
We rarely give feedback on designs during the design process. We are working on many website projects and do not have the time to provide feedback. We usually respond if your request is well thought out and asks specific questions, but a note asking “feedback, please” usually goes unanswered.

```html
<!DOCTYPE html>
<html lang="en">
<head>
<meta charset="utf-8">
<title>Fernmoor Elementary School PTA</title>
<link href="https://fonts.googleapis.com/css2?family=Playfair+Display:ital,wght@0,400;0,500;1,400&family=Inter:wght@400;500&display=swap" rel="stylesheet">
<style>
:root{
  --navy:#1f3a8a;
  --ink:#1c2233;
  --text:#4a5163;
  --muted:#6b7280;
  --line:#e5e7eb;
  --soft:#f7f8fb;
  --footer:#141a33;
  --footer-text:#c9cedb;
  --white:#ffffff;
}
*{box-sizing:border-box;margin:0;padding:0}
html,body{width:1200px;height:5222px;overflow:hidden;background:var(--white)}
body{position:relative;font-family:'Inter',sans-serif;color:var(--text)}
.serif{font-family:'Playfair Display',serif}
.abs{position:absolute}
.center{left:0;width:1200px;text-align:center}
h1,h2,h3{font-family:'Playfair Display',serif;font-weight:400;color:var(--ink)}
.divider{position:absolute;left:540px;width:120px;height:8px}
.divider::before{content:"";position:absolute;left:0;right:0;top:3.5px;height:1px;background:#c9cfdd}
.divider::after{content:"";position:absolute;left:57px;top:1px;width:6px;height:6px;border-radius:50%;background:var(--navy);box-shadow:0 0 0 5px var(--white)}
.divider.on-soft::after{box-shadow:0 0 0 5px var(--soft)}
.divider.on-dark::before{background:rgba(255,255,255,.5)}
.divider.on-dark::after{background:#fff;box-shadow:0 0 0 5px #6a6a6a}

/* nav */
.site-nav{position:absolute;top:0;left:0;width:1200px;height:71px;border-bottom:1px solid var(--line)}
.brand{position:absolute;left:60px;top:22px;display:flex;align-items:center;gap:8px;font-family:'Playfair Display',serif;font-size:17px;color:var(--navy)}
.brand-mark{width:14px;height:14px;background:var(--navy)}
.nav-links{position:absolute;top:28px;left:0;width:1200px;text-align:center;font-family:'Playfair Display',serif;font-size:13px;color:var(--text)}
.nav-links span{margin:0 20px}

/* hero */
.hero-title{top:158px;font-size:54px;line-height:56px}
.hero-sub{top:328px;font-size:16px;line-height:29px}
.hero-photo{top:470px;left:0;width:1200px;height:444px;background:linear-gradient(100deg,#3f7d8a 0%,#8bb3e0 30%,#5a82c4 55%,#8cb2e4 75%,#c9a640 100%);box-shadow:0 14px 28px rgba(0,0,0,.18)}

/* what we do */
.glow{border-radius:50%;background:radial-gradient(circle,rgba(200,206,222,.35),rgba(255,255,255,0) 70%)}
.wwd-title{top:1070px;font-size:42px}
.wwd-text{top:1196px;font-size:16px;line-height:29px}
.card{position:absolute;width:355px;height:215px;border:1px solid var(--line);background:var(--white);padding:30px}
.card-icon{width:46px;height:46px;border-radius:50%;background:#eef0f7;display:flex;align-items:center;justify-content:center}
.card h3{margin-top:30px;font-size:20px}
.card p{margin-top:10px;font-size:13px;line-height:22px;width:220px}

/* news section */
.news-panel{top:2031px;left:89px;width:1022px;height:1589px;background:var(--soft)}
.feature{top:2055px;left:117px;width:966px;height:443px;background:linear-gradient(180deg,#6a7a4a 0%,#5b6b3c 45%,#3f4a2a 100%);box-shadow:0 10px 24px rgba(0,0,0,.2)}
.feature-shade{position:absolute;inset:0;background:linear-gradient(180deg,rgba(0,0,0,0) 40%,rgba(0,0,0,.55))}
.feature-date{left:43px;top:260px;color:#fff;font-size:12px;letter-spacing:1px;display:flex;align-items:center;gap:6px}
.feature-title{left:43px;top:290px;color:#fff;font-size:42px}
.feature-text{left:43px;top:348px;width:680px;color:#fff;font-size:15px;line-height:25px}
.news-title{top:2585px;font-size:42px}
.news-card{position:absolute;top:2697px;width:462px;text-align:center}
.news-img{height:228px}
.news-card h3{margin-top:24px;font-size:24px}
.news-card p{margin:10px auto 0;width:420px;font-size:13px;line-height:23px}
.hl-title{top:3122px;font-size:42px;display:flex;justify-content:center;align-items:center;gap:16px}
.hl-table{top:3238px;left:258px;width:682px;height:382px;background:#fff;box-shadow:0 6px 22px rgba(0,0,0,.12);padding:22px 46px}
.hl-row{display:flex;align-items:center;height:68px;border-bottom:1px solid var(--line)}
.hl-row:last-child{border-bottom:none}
.hl-date{width:68px;font-size:11px;color:var(--muted)}
.hl-name{flex:1;font-size:14px;color:var(--ink)}
.hl-val{font-family:'Playfair Display',serif;font-size:16px;color:var(--navy)}

/* cta */
.cta{top:3705px;left:0;width:1200px;height:580px;background:linear-gradient(90deg,#5f6064,#6e6e70 40%,#6a6a6a)}
.cta-title{top:3890px;font-size:58px;color:#fff}
.cta-text{top:3984px;font-size:16px;line-height:28px;color:#eef}
.cta-btn{top:4088px;left:530px;width:139px;height:55px;border:1px solid #fff;color:#fff;font-size:15px;display:flex;align-items:center;justify-content:center;gap:10px}

/* newsletter */
.news-band{top:4285px;left:0;width:1200px;height:502px;background:linear-gradient(180deg,#fff,#f3f4f8)}
.mail-icon{top:4371px;left:573px;width:54px;height:54px;border-radius:50%;background:#e8eaf2;display:flex;align-items:center;justify-content:center}
.stay-title{top:4453px;font-size:44px}
.stay-text{top:4551px;font-size:15px;line-height:27px}
.signup{top:4650px;left:401px;width:396px;height:48px;display:flex;box-shadow:0 6px 16px rgba(0,0,0,.12)}
.signup-input{flex:1;background:#fff;border:1px solid var(--line);font-size:13px;color:#9aa0ad;display:flex;align-items:center;padding-left:22px}
.signup-btn{width:124px;background:var(--navy);color:#fff;font-size:14px;display:flex;align-items:center;justify-content:center}

/* footer */
.footer{top:4787px;left:0;width:1200px;height:435px;background:var(--footer);color:var(--footer-text)}
.foot-head{font-family:'Playfair Display',serif;font-size:11px;letter-spacing:2px;color:#8a90a6}
.foot-item{display:flex;gap:12px;font-size:13.5px;line-height:20px;margin-top:14px}
.foot-links div{font-size:13.5px;margin-top:13px}
.foot-brand{right:120px;top:66px;display:flex;align-items:center;gap:8px;font-family:'Playfair Display',serif;font-size:20px;color:#fff}
.foot-brand i{width:14px;height:14px;background:#fff;display:block}
.foot-tag{right:120px;top:144px;text-align:right;font-family:'Playfair Display',serif;font-style:italic;font-size:13px;line-height:22px;color:#8a90a6}
.social{top:196px;width:30px;height:30px;border:1px solid #5a6180;border-radius:50%}
.social::after{content:"";position:absolute;left:11px;top:11px;width:6px;height:6px;border-radius:50%;background:#c9cedb}
.copyright{top:355px;font-size:12px;color:#8a90a6}
</style>
</head>
<body>

<header class="site-nav">
  <div class="brand"><span class="brand-mark"></span>Fernmoor</div>
  <nav class="nav-links"><span>About</span><span>Events</span><span>Get Involved</span><span>Board</span><span>Contact</span></nav>
</header>

<h1 class="abs center hero-title">Fernmoor Elementary School<br>Parent Teacher Association</h1>
<div class="divider" style="top:291px"></div>
<p class="abs center hero-sub">Building stronger connections between parents, teachers, and<br>students through community, engagement, and shared purpose</p>
<div class="abs hero-photo" role="img" aria-label="Photo of two schoolgirls in blue uniforms chatting in class"></div>

<div class="abs glow" style="left:820px;top:960px;width:520px;height:520px"></div>
<div class="abs glow" style="left:-160px;top:1500px;width:520px;height:520px"></div>
<h2 class="abs center wwd-title">What We Do</h2>
<div class="divider" style="top:1133px"></div>
<p class="abs center wwd-text">The Fernmoor Elementary PTA is dedicated to enriching the educational experience of<br>every student through community engagement, fundraising, advocacy, and fostering<br>meaningful connections between families and educators.</p>

<div class="card" style="left:231px;top:1342px">
  <div class="card-icon"><svg width="20" height="20" viewBox="0 0 24 24" fill="none" stroke="#1f3a8a" stroke-width="1.8"><path d="M12 20s-7-4.4-7-10a4 4 0 0 1 7-2.6A4 4 0 0 1 19 10c0 5.6-7 10-7 10z"/></svg></div>
  <h3>Support Our Students</h3><p>Join our volunteer program and support classroom activities</p>
</div>
<div class="card" style="left:614px;top:1342px">
  <div class="card-icon"><svg width="20" height="20" viewBox="0 0 24 24" fill="none" stroke="#1f3a8a" stroke-width="1.8"><circle cx="9" cy="8" r="3.5"/><path d="M3 19c0-3.3 2.7-5.5 6-5.5s6 2.2 6 5.5"/><path d="M15 4.8a3.3 3.3 0 0 1 0 6.4M17 13.8c2.4.6 4 2.5 4 5.2"/></svg></div>
  <h3>Community Engagement</h3><p>Experience the impact of active parent involvement</p>
</div>
<div class="card" style="left:231px;top:1585px">
  <div class="card-icon"><svg width="20" height="20" viewBox="0 0 24 24" fill="none" stroke="#1f3a8a" stroke-width="1.8"><path d="M9 17h6M10 20.5h4M12 3a6 6 0 0 0-3.5 10.9V15h7v-1.1A6 6 0 0 0 12 3z"/></svg></div>
  <h3>Enrichment Programs</h3><p>Programs designed to meet every family's needs</p>
</div>
<div class="card" style="left:614px;top:1585px">
  <div class="card-icon"><svg width="20" height="20" viewBox="0 0 24 24" fill="none" stroke="#1f3a8a" stroke-width="1.8"><path d="M3 12l5-5 4 2 4-3 5 5-7 7-4-3z"/><path d="M9 13l3 2M12 11l3 2"/></svg></div>
  <h3>Stronger Together</h3><p>Build relationships that strengthen our school community</p>
</div>

<div class="abs news-panel"></div>
<div class="abs feature" role="img" aria-label="Photo of children dancing around a ribboned maypole at a fall fair">
  <div class="feature-shade"></div>
  <div class="abs feature-date"><svg width="14" height="14" viewBox="0 0 24 24" fill="none" stroke="#fff" stroke-width="2"><rect x="3" y="5" width="18" height="16" rx="2"/><path d="M3 10h18M8 3v4M16 3v4"/></svg>OCTOBER 28, 2024</div>
  <div class="abs feature-title serif">Fall Festival</div>
  <p class="abs feature-text">Join us for our annual Fall Festival featuring games, food trucks, pumpkin decorating, and family fun activities for all ages.</p>
</div>

<h2 class="abs center news-title">The Latest News</h2>
<div class="divider on-soft" style="top:2647px"></div>
<article class="news-card" style="left:117px">
  <div class="news-img" role="img" aria-label="Photo of an audience at an award ceremony in a hall" style="background:linear-gradient(180deg,#d9dde6,#7a7f8c 55%,#2c2f38)"></div>
  <h3>FY24 Award Winners</h3><p>Congratulations to our outstanding volunteers who have made a significant impact this year.</p>
</article>
<article class="news-card" style="left:621px">
  <div class="news-img" role="img" aria-label="Portrait photo of a new board member by a lake" style="background:linear-gradient(90deg,#5d7a8c,#a88570 50%,#6f8895)"></div>
  <h3>Meet Our New Board Members</h3><p>We are excited to introduce our newly elected board members for the 2024-25 school year.</p>
</article>

<h2 class="abs center hl-title"><svg width="22" height="22" viewBox="0 0 24 24" fill="none" stroke="#1f3a8a" stroke-width="2"><path d="M3 17l6-6 4 4 7-7M15 8h5v5"/></svg>2025 Event Highlights</h2>
<div class="divider on-soft" style="top:3188px"></div>
<div class="abs hl-table">
  <div class="hl-row"><span class="hl-date">Mar 15</span><span class="hl-name">Spring Fundraiser - Record Breaking</span><span class="hl-val">$45K</span></div>
  <div class="hl-row"><span class="hl-date">Dec 10</span><span class="hl-name">Winter Concert - Sold Out</span><span class="hl-val">500+ Attendees</span></div>
  <div class="hl-row"><span class="hl-date">Nov 18</span><span class="hl-name">Book Fair - Best Year Ever</span><span class="hl-val">$12K Raised</span></div>
  <div class="hl-row"><span class="hl-date">May 22</span><span class="hl-name">Field Day - Community Building</span><span class="hl-val">450 Participants</span></div>
  <div class="hl-row"><span class="hl-date">Sep 08</span><span class="hl-name">Parent Education Night</span><span class="hl-val">200+ Families</span></div>
</div>

<div class="abs cta" role="img" aria-label="Muted photo of a stack of books"></div>
<div class="divider on-dark" style="top:3843px"></div>
<h2 class="abs center cta-title" style="color:#fff">All voices are welcome here!</h2>
<p class="abs center cta-text">Join our community of dedicated parents and teachers making a<br>difference in our children's lives</p>
<div class="abs cta-btn">Join us <svg width="14" height="14" viewBox="0 0 24 24" fill="none" stroke="#fff" stroke-width="2"><path d="M5 12h14M13 6l6 6-6 6"/></svg></div>

<div class="abs news-band"></div>
<div class="abs mail-icon"><svg width="24" height="24" viewBox="0 0 24 24" fill="none" stroke="#1f3a8a" stroke-width="1.8"><rect x="3" y="5" width="18" height="14" rx="2"/><path d="M3 7l9 6 9-6"/></svg></div>
<h2 class="abs center stay-title">Stay Connected</h2>
<div class="divider" style="top:4522px;background:transparent"></div>
<p class="abs center stay-text">Subscribe to our newsletter and receive monthly updates about<br>events, volunteer opportunities, and important school news.</p>
<div class="abs signup"><div class="signup-input">Enter your email address</div><div class="signup-btn">Subscribe</div></div>

<footer class="abs footer">
  <div class="abs" style="left:115px;top:63px">
    <div class="foot-head">CONTACT US</div>
    <div class="foot-item" style="margin-top:22px"><svg width="14" height="14" viewBox="0 0 24 24" fill="none" stroke="#c9cedb" stroke-width="2"><path d="M12 21s-7-6-7-11a7 7 0 0 1 14 0c0 5-7 11-7 11z"/><circle cx="12" cy="10" r="2.5"/></svg><span>Fernmoor Elementary School<br>48 Orchard Row<br>Brindlewood, CA 95000</span></div>
    <div class="foot-item"><svg width="14" height="14" viewBox="0 0 24 24" fill="none" stroke="#c9cedb" stroke-width="2"><path d="M5 4h4l2 5-3 2a11 11 0 0 0 5 5l2-3 5 2v4a2 2 0 0 1-2 2A17 17 0 0 1 3 6a2 2 0 0 1 2-2z"/></svg><span>(555) 014-2290</span></div>
    <div class="foot-item"><svg width="14" height="14" viewBox="0 0 24 24" fill="none" stroke="#c9cedb" stroke-width="2"><rect x="3" y="5" width="18" height="14" rx="2"/><path d="M3 7l9 6 9-6"/></svg><span>info@fernmoorpta.org</span></div>
  </div>
  <div class="abs foot-links" style="left:450px;top:63px">
    <div class="foot-head" style="margin-top:0">QUICK LINKS</div>
    <div style="margin-top:22px">About Us</div><div>Events</div><div>Get Involved</div><div>Board Members</div><div>Resources</div>
  </div>
  <div class="abs foot-brand"><i></i>Fernmoor</div>
  <div class="abs foot-tag">Building stronger communities<br>through education</div>
  <span class="abs social" style="left:947px"></span>
  <span class="abs social" style="left:996px"></span>
  <span class="abs social" style="left:1046px"></span>
  <div class="abs center copyright">© 2024 Fernmoor Elementary School PTA. All rights reserved.</div>
</footer>

</body>
</html>
```